business card double side design

We need a business card design for our company PLUMlearnhub. DOUBLE SIDED. We provide continuing education programs & courses across North America. Our website is www.plumlearnhub.example - please use the grey pinstrip concept as part of the design. Compliment the branding that is occuring on that site!
Please use pantones daa520 and 3f3151. Verdana for text. I have attached our logo.
I would like the logo & website address www.PLUMlearnhub.example on the front of the card, all other info on the backside. The final design should communicate authority and credibility.

• verdanda

• pantones daa520 and 3f3151. Verdana for text.
• must compliment the branding occuring on the www.PLUMlearnhub.example

```html
<!DOCTYPE html>
<html lang="en">
<head>
<meta charset="utf-8">
<title>PLUMlearnhub business card – front and back</title>
<link rel="stylesheet" href="https://fonts.googleapis.com/css2?family=Noto+Sans:wght@400;700&display=swap">
<style>
  :root {
    --plum: #3f3151;
    --gold: #daa520;
    --charcoal: #302d2e;
    --text-grey: #6a6a6a;
    --stripe-light: #f6f7f8;
    --stripe-dark: #e6e7e9;
    --card-edge: #d8d8d8;
    --card-shadow: #d2d2d2;
    --label: #3d4a22;
    --page: #ffffff;
  }
  html, body {
    margin: 0;
    padding: 0;
    width: 1200px;
    height: 901px;
    overflow: hidden;
    background: var(--page);
  }
  .canvas {
    position: relative;
    width: 1200px;
    height: 901px;
    font-family: Verdana, "Noto Sans", sans-serif;
  }
  .card {
    position: absolute;
    left: 298px;
    width: 592px;
    height: 364px;
    box-sizing: border-box;
    border: 1px solid var(--card-edge);
    box-shadow: 8px 8px 0 var(--card-shadow);
    background: repeating-linear-gradient(90deg,
      var(--stripe-light) 0px,
      var(--stripe-light) 12px,
      var(--stripe-dark) 22px,
      var(--stripe-light) 33px,
      var(--stripe-light) 38px);
    overflow: hidden;
  }
  .card--front { top: 60px; }
  .card--back { top: 474px; }

  .band-top {
    position: absolute; left: 0; right: 0; top: 1px;
    height: 31px; background: var(--plum);
    border-bottom: 8px solid var(--gold);
  }
  .band-bottom {
    position: absolute; left: 0; right: 0; bottom: 1px;
    height: 33px; background: var(--charcoal);
    border-top: 8px solid var(--gold);
  }

  .brand {
    position: absolute;
    left: 110px; top: 93px;
    width: 400px;
    display: flex; align-items: center; gap: 24px;
  }
  .brand__mark { display: block; flex: none; }
  .brand__name {
    font-weight: 700;
    font-size: 29px;
    color: var(--gold);
    white-space: nowrap;
  }
  .website {
    position: absolute; left: 0; right: 0; top: 282px;
    margin: 0;
    text-align: center;
    font-size: 18px;
    color: var(--text-grey);
  }

  .person { position: absolute; left: 0; right: 0; top: 80px; text-align: center; }
  .person__name { font-size: 19px; font-weight: 700; color: var(--plum); line-height: 24px; }
  .person__title { font-size: 21px; color: var(--gold); line-height: 24px; }

  .office {
    position: absolute; left: 0; right: 0; top: 197px;
    text-align: center; font-style: normal;
  }
  .office__heading { font-size: 20px; font-weight: 700; color: var(--plum); line-height: 22px; }
  .office__line { font-size: 19px; color: var(--text-grey); line-height: 21px; }

  .side-label {
    position: absolute; left: 916px;
    font-family: "Noto Sans", sans-serif;
    font-size: 18px;
    color: var(--label);
  }
  .side-label--front { top: 410px; }
  .side-label--back { top: 825px; }
</style>
</head>
<body>
<main class="canvas">

  <section class="card card--front" aria-label="Card front">
    <div class="band-top"></div>
    <div class="brand">
      <svg class="brand__mark" width="130" height="130" viewBox="0 0 130 130" aria-hidden="true">
        <circle cx="65" cy="65" r="63" fill="var(--gold)"/>
      </svg>
      <span class="brand__name">PLUMlearnhub</span>
    </div>
    <p class="website">www.PLUMlearnhub.example</p>
    <div class="band-bottom"></div>
  </section>
  <span class="side-label side-label--front">front</span>

  <section class="card card--back" aria-label="Card back">
    <div class="band-top"></div>
    <div class="person">
      <div class="person__name">Dana Whitlock</div>
      <div class="person__title">Technical Consultant</div>
    </div>
    <address class="office">
      <div class="office__heading">Canada Headquarters</div>
      <div class="office__line">Suite 140, 82 Orchard Crescent</div>
      <div class="office__line">Maplewood, AB. T0X 1A0</div>
      <div class="office__line">Tel: (780) 555-0142</div>
      <div class="office__line">Email: support@PLUMlearnhub.example</div>
    </address>
    <div class="band-bottom"></div>
  </section>
  <span class="side-label side-label--back">back</span>

</main>
</body>
</html>
```